We need a tri-fold brochure for our business called: KindlePath. (KindlePath Therapy Services)
This is a therapy services business that offers Physiotherapy and Occupational Therapy to children aged 5 to 16 years of age. The focus is on Neuro-developmental therapy and the children have a range of conditions such as Cerebral-Palsy, brain injuries etc... We are looking for designs that focus on children, fun and the word nurture.
Target Market(s)
Primarily parents and people looking for therapy services.
Industry/Entity Type
Business
Font styles to use
Sans Serif

```html
<!DOCTYPE html>
<html lang="en">
<head>
<meta charset="UTF-8">
<title>KindlePath Therapy Services – Tri-fold Brochure</title>
<link rel="stylesheet" href="https://fonts.googleapis.com/css2?family=Open+Sans:wght@400;600&family=Ubuntu:wght@500;700&display=swap">
<style>
  :root{
    --page:#eef0f2;
    --sky-top:#cfe6f7;
    --sky-bottom:#f4f9fd;
    --green:#2e9e48;
    --green-dark:#23853b;
    --orange:#f39422;
    --blue:#1f86c6;
    --text:#555a5e;
    --rule:#9aa3aa;
    --white:#ffffff;
  }
  *{box-sizing:border-box;margin:0;padding:0}
  html,body{width:940px;height:1200px;overflow:hidden;background:var(--page)}
  body{font-family:"Open Sans",sans-serif;color:var(--text)}
  .brochure{position:absolute;left:20px;top:282px;width:900px;height:635px;overflow:hidden;
    box-shadow:0 6px 18px rgba(0,0,0,.18);background:var(--white)}
  .panel{position:absolute;top:0;width:300px;height:635px}
  .panel--about{left:0;background:linear-gradient(180deg,var(--sky-top),var(--sky-bottom) 70%)}
  .panel--contact{left:300px;background:linear-gradient(180deg,var(--sky-top),var(--sky-bottom) 70%);
    border-left:1px solid rgba(255,255,255,.6)}
  .panel--cover{left:600px;background:linear-gradient(180deg,#ffffff,#eef3f7)}
  .photo{position:absolute;left:600px;top:114px;width:300px;height:360px;
    background:linear-gradient(160deg,#dfe7ec 0%,#b9c6cf 45%,#8a8f93 100%)}
  .illustration{position:absolute;left:20px;top:380px;width:240px;height:200px;
    background:radial-gradient(ellipse at 50% 55%,rgba(247,148,29,.35),rgba(46,158,72,.18) 55%,rgba(255,255,255,0) 75%)}
  .hill{position:absolute;left:0;top:0;width:900px;height:635px}
  .heading{font-family:"Ubuntu",sans-serif;font-weight:700;font-size:19px;text-transform:uppercase;
    letter-spacing:.2px;position:absolute;left:23px;width:252px;padding-bottom:3px;border-bottom:1px solid var(--rule)}
  .heading--about{top:38px;color:var(--orange)}
  .heading--team{top:242px;color:var(--green)}
  .heading--contact{left:325px;width:250px;top:242px;color:var(--blue);text-align:center;border-bottom:none}
  .copy{position:absolute;font-size:9.4px;line-height:13.2px;text-align:justify}
  .copy p+p{margin-top:13px}
  .copy--about{left:23px;top:72px;width:252px}
  .copy--team{left:23px;top:275px;width:252px}
  .copy--intro{left:323px;top:57px;width:254px}
  .copy--contact{left:323px;top:275px;width:254px}
  .contact-list{position:absolute;left:300px;top:318px;width:300px;list-style:none;text-align:center;font-size:9.4px}
  .contact-list li{height:41px;display:flex;flex-direction:column;align-items:center}
  .contact-list svg{width:9px;height:9px;margin-bottom:5px}
  .wordmark{font-family:"Ubuntu",sans-serif;font-weight:700;position:absolute;text-align:center;white-space:nowrap}
  .wordmark--back{left:300px;width:300px;top:522px;font-size:38px;color:var(--white)}
  .wordmark--cover{left:600px;width:300px;top:30px;font-size:44px;color:var(--green)}
  .tagline{position:absolute;left:600px;width:300px;text-align:center;color:var(--white)}
  .tagline__title{font-family:"Ubuntu",sans-serif;font-weight:700;font-size:31px;top:518px;position:absolute;width:100%}
  .tagline__sub{font-size:18px;top:560px;position:absolute;width:100%;letter-spacing:.5px}
  .web{position:absolute;top:603px;width:300px;display:flex;align-items:center;justify-content:center;gap:8px;
    color:var(--white);font-size:14px;letter-spacing:.3px}
  .web::before,.web::after{content:"";width:28px;height:1px;background:var(--white)}
  .web--1{left:0}.web--2{left:300px}.web--3{left:600px}
</style>
</head>
<body>
<main class="brochure">
  <section class="panel panel--about"></section>
  <section class="panel panel--contact"></section>
  <section class="panel panel--cover"></section>

  <div class="photo" role="img" aria-label="Photo of a smiling therapist gently stretching the leg of a young child lying on a treatment bed"></div>
  <div class="illustration" role="img" aria-label="Illustration of a cheerful girl riding a bicycle up a grassy hill while flying a kite"></div>

  <svg class="hill" viewBox="0 0 900 635" aria-hidden="true">
    <path d="M0,552 Q280,462 600,440 L900,452 L900,635 L0,635 Z" fill="var(--orange)"/>
    <path d="M0,566 Q280,474 600,452 L900,464 L900,635 L0,635 Z" fill="var(--green)"/>
    <path d="M0,600 Q300,520 600,500 L900,505 L900,635 L0,635 Z" fill="var(--green-dark)" opacity=".25"/>
    <line x1="300" y1="470" x2="300" y2="635" stroke="#ffffff" stroke-opacity=".25"/>
    <line x1="600" y1="440" x2="600" y2="635" stroke="#ffffff" stroke-opacity=".25"/>
  </svg>

  <h2 class="heading heading--about">About Us</h2>
  <div class="copy copy--about">
    <p>It is a long established fact that a reader will be distracted by the readable content of a page when looking at its layout. The point of using Lorem Ipsum is that it has a more-or-less normal distribution of letters, as opposed to using 'Content here, content here', making it look like readable English.</p>
    <p>It is a long established fact that a reader will be distracted by the readable content of a page when looking at its layout. The point of using Lorem Ipsum is that it has a more-or-less.</p>
  </div>

  <h2 class="heading heading--team">Our Team</h2>
  <div class="copy copy--team">
    <p>It is a long established fact that a reader will be distracted by the readable content of a page when looking at its layout. The point of using Lorem Ipsum is that it has a more-or-less normal distribution of letters, as opposed to using 'Content here, content here', making it look like readable English.</p>
  </div>

  <div class="copy copy--intro">
    <p>Lorem ipsum dolor sit amet, consectetur adipiscing elit, sed do eiusmod tempor incididunt ut labore et dolore magna aliqua. Ut enim ad minim veniam, quis nostrud exercitation ullamco laboris nisi ut aliquip ex ea commodo consequat.</p>
    <p>Lorem ipsum dolor sit amet, consectetur adipiscing elit, sed do eiusmod tempor incididunt ut labore et dolore magna aliqua. Ut enim ad minim veniam, quis nostrud exercitation</p>
  </div>

  <h2 class="heading heading--contact">Get in touch with us!</h2>
  <div class="copy copy--contact">
    <p>Lorem ipsum dolor sit amet, consectetur adipiscing elit, sed do eiusmod tempor incididunt ut labore et dolore</p>
  </div>

  <ul class="contact-list">
    <li>
      <svg viewBox="0 0 10 10"><path d="M5 0a3.5 3.5 0 0 0-3.5 3.5C1.5 6 5 10 5 10s3.5-4 3.5-6.5A3.5 3.5 0 0 0 5 0zm0 5a1.4 1.4 0 1 1 0-2.8A1.4 1.4 0 0 1 5 5z" fill="var(--orange)"/></svg>
      <span>42 Meadowlark Lane, Brookfield, GA, 30512</span>
    </li>
    <li>
      <svg viewBox="0 0 10 10"><path d="M2 .5l2 2-1 1.3a6 6 0 0 0 3.2 3.2l1.3-1 2 2L8 9.5C4 9.5.5 6 .5 2z" fill="var(--orange)"/></svg>
      <span>555-014-227 / 555-019-348</span>
    </li>
    <li>
      <svg viewBox="0 0 10 10"><rect x="0.5" y="2" width="9" height="6.5" rx="1" fill="var(--orange)"/><path d="M1 2.6l4 3 4-3" stroke="#fff" stroke-width=".8" fill="none"/></svg>
      <span>hello@kindlepath.example</span>
    </li>
  </ul>

  <div class="wordmark wordmark--back">KindlePath</div>
  <div class="wordmark wordmark--cover">KindlePath</div>

  <div class="tagline">
    <div class="tagline__title">LOREM IPSUM</div>
    <div class="tagline__sub">IS SIMPLY DUMMY TEXT</div>
  </div>

  <div class="web web--1">WWW.KINDLEPATH.EXAMPLE</div>
  <div class="web web--2">WWW.KINDLEPATH.EXAMPLE</div>
  <div class="web web--3">WWW.KINDLEPATH.EXAMPLE</div>
</main>
</body>
</html>
```